Brightmarket Web Demo Clickthru

Create a realistic web demo to demonstrate our Tradeloop Platform.
There is no back end required.
This Demo will shown to Senior M&A or R&D Executives.
Student entrepreneurs will also see this demo.
There are several attachment to this spec.
Two most important are
Demo User Spec and Demo Flow word documents.
Other attaches are images to give you some idea of the content for specific areas of the site. This will require a walkthrough with selected designer.
Updates

Target Market(s)

See Brief

Industry/Entity Type

Venture Capital

Number of Pages Required

5+ page

Font styles to use
Sans Serif

Colors
32a5d7
33a6d7
0255a3
0692cd
85abd2
f37122
000000
474747
919191

Requirements
Must have
• See Brief
Nice to have
• See Briefs
Should not have
• See Briefs

```html
<!DOCTYPE html>
<html lang="en">
<head>
<meta charset="utf-8">
<title>Brightmarket — Tradeloop Platform</title>
<link href="https://fonts.googleapis.com/css2?family=Open+Sans:wght@400;600;700&family=Oswald:wght@400;500&display=swap" rel="stylesheet">
<style>
:root{
  --sky:#32a5d7;--blue:#0692cd;--navy:#0255a3;--soft:#85abd2;--orange:#f37122;
  --ink:#000;--text:#474747;--muted:#919191;--dark:#2b2f33;--darker:#1f2226;--line:#e4e6e8;
}
*{box-sizing:border-box;margin:0;padding:0}
html,body{width:726px;height:1200px;overflow:hidden}
body{font-family:"Open Sans",Arial,sans-serif;color:var(--text);background:#fff;position:relative;font-size:7px}
.abs{position:absolute}
.topbar{top:0;left:0;width:726px;height:20px;background:var(--darker);display:flex;align-items:center;justify-content:space-between;padding:0 97px;color:#cfd3d6;font-size:6px}
.topbar .soc{display:flex;gap:5px}
.topbar .soc span{width:9px;height:9px;border-radius:50%;background:var(--sky);display:block}
.header{top:20px;left:0;width:726px;height:52px;background:#fff;display:flex;align-items:center;justify-content:space-between;padding:0 97px}
.brand{display:flex;align-items:center;gap:6px;font-weight:700;font-size:17px;color:var(--navy)}
.brand i{width:14px;height:14px;background:var(--sky);display:block}
.search{display:flex;flex-direction:column;align-items:flex-end;gap:4px}
.search .row{display:flex}
.search .field{width:150px;height:15px;border:1px solid var(--line)}
.search .go{width:34px;height:15px;background:var(--orange);color:#fff;font-size:6px;display:flex;align-items:center;justify-content:center}
.search small{font-size:5.5px;color:var(--muted)}
.nav{top:72px;left:0;width:726px;height:18px;background:var(--dark);display:flex;align-items:center;padding-left:97px;font-family:"Oswald",sans-serif;font-size:6.5px;color:#e8eaec;letter-spacing:.3px}
.nav a{padding:0 9px;height:18px;display:flex;align-items:center}
.nav a.on{background:#3c4146}
.nav .signup{margin-left:auto;margin-right:97px;background:var(--orange);padding:0 12px}
.hero{top:90px;left:0;width:726px;height:175px;background:radial-gradient(circle at 50% 40%,#8a8f94,#4b5055 55%,#2f3337)}
.arrow{width:22px;height:34px;background:var(--orange);top:292px}
.card{top:208px;width:260px;height:160px;background:#fff;box-shadow:0 1px 5px rgba(0,0,0,.25)}
.card h3{height:18px;background:var(--blue);color:#fff;font-family:"Oswald",sans-serif;font-weight:500;font-size:8px;padding:0 8px;display:flex;align-items:center}
.card ul{list-style:none;padding:4px 8px}
.card li{display:flex;align-items:center;height:24px;border-bottom:1px solid var(--line);gap:7px}
.card li .ic{width:12px;height:12px;border-radius:50%;border:1px solid var(--orange)}
.card li b{display:block;font-size:6px;color:var(--navy)}
.card li span{font-size:5px;color:var(--muted)}
.card li .tx{flex:1}
.card li .go{width:11px;height:11px;background:var(--orange)}
.card .more{margin:5px auto 0;width:40px;height:9px;background:var(--line)}
.intro{top:410px;left:0;width:726px;text-align:center}
.intro h2{font-family:"Oswald",sans-serif;font-weight:400;font-size:15px;color:var(--text);letter-spacing:.5px}
.intro h2 em{font-style:normal;color:var(--blue)}
.intro .rule{width:36px;height:2px;background:var(--orange);margin:6px auto}
.intro p{width:430px;margin:8px auto 0;font-size:5.5px;line-height:1.6;color:var(--muted)}
.bulb-art{top:420px;left:606px;width:64px;height:80px;background:linear-gradient(180deg,#f1f3f5,#e3e7ea)}
.band{top:545px;left:0;width:726px;height:140px}
.tiles{top:588px;left:110px;display:flex;gap:18px}
.tile{width:68px;height:56px;background:#fff;display:flex;align-items:center;justify-content:center}
.tile i{width:28px;height:28px;display:block}
.app{top:742px;left:97px;width:270px}
.app h2{font-family:"Oswald",sans-serif;font-weight:400;font-size:13px;color:var(--text)}
.app h2 em{font-style:normal;color:var(--blue)}
.app .rule{width:30px;height:2px;background:var(--orange);margin:6px 0 10px}
.app p{font-size:5.5px;line-height:1.6;color:var(--muted);margin-bottom:6px}
.app .btns{display:flex;gap:8px;margin-top:10px}
.btn{width:76px;height:17px;font-size:6px;color:#fff;display:flex;align-items:center;justify-content:center}
.btn.or{background:var(--orange)}.btn.gr{background:#c9ccce}
.video{top:775px;left:380px;width:249px;height:135px;background:#3a3f44}
.video .ttl{height:14px;background:#2a2e32;color:#e8eaec;font-family:"Oswald",sans-serif;font-size:7px;display:flex;align-items:center;padding-left:7px}
.video .stage{top:14px;left:0;width:249px;height:107px;background:#fff;display:flex;align-items:center;justify-content:center}
.video .ctrl{bottom:0;left:0;width:249px;height:14px;background:#2a2e32;display:flex;align-items:center;gap:5px;padding:0 6px}
.video .ctrl i{display:block;height:3px;background:var(--sky);width:140px}
.follow{top:955px;left:0;width:726px;height:35px;background:var(--blue);display:flex;align-items:center;justify-content:space-between;padding:0 97px;font-family:"Oswald",sans-serif;font-size:9px;color:#fff}
.follow .soc{display:flex;gap:5px}
.follow .soc span{width:14px;height:14px;border-radius:50%;background:#fff;opacity:.9}
.footer{top:990px;left:0;width:726px;height:190px;background:var(--dark);display:flex;padding:22px 97px 0;gap:30px;color:#aeb3b8}
.footer .col{font-size:5.5px;line-height:2}
.footer h4{font-family:"Oswald",sans-serif;font-weight:400;color:#fff;font-size:7.5px;border-bottom:1px solid #4a5056;margin-bottom:5px;width:70px}
.footer .fbrand{width:150px}
.footer .fbrand .brand{color:#fff;font-size:14px}
.footer .fbrand p{margin-top:8px;line-height:1.7}
.copy{top:1180px;left:0;width:726px;height:20px;background:var(--darker);color:var(--muted);font-size:5.5px;display:flex;align-items:center;justify-content:center}
</style>
</head>
<body>
<div class="abs topbar"><div class="soc"><span></span><span></span><span></span><span></span></div><div>Welcome, Guest&nbsp;&nbsp;|&nbsp;&nbsp;My Account&nbsp;&nbsp;|&nbsp;&nbsp;Contact</div></div>
<header class="abs header">
  <div class="brand"><i></i>Brightmarket</div>
  <div class="search"><div class="row"><div class="field"></div><div class="go">SEARCH</div></div><small>Advanced search&nbsp;&nbsp;·&nbsp;&nbsp;Forgot password?</small></div>
</header>
<nav class="abs nav"><a class="on">HOME</a><a>JOIN FOR SCHOOLS</a><a>MY SCHOOLS</a><a>STUDENT COMPANIES</a><a>TRADELOOP SPONSORS</a><a>ABOUT</a><a>CONTACT</a><a class="signup">SIGN UP</a></nav>
<div class="abs hero" role="img" aria-label="Hand presenting a glowing light bulb on a dark grey background"></div>
<div class="abs arrow" style="left:0"></div><div class="abs arrow" style="right:0"></div>

<section class="abs card" style="left:97px">
  <h3>NEW STARTUP LISTINGS</h3>
  <ul>
    <li><i class="ic"></i><div class="tx"><b>Solar Grid Labs</b><span>Clean energy storage for homes</span></div><i class="go"></i></li>
    <li><i class="ic"></i><div class="tx"><b>Medi Track</b><span>Patient records on any device</span></div><i class="go"></i></li>
    <li><i class="ic"></i><div class="tx"><b>Aero Parcel</b><span>Drone delivery for campuses</span></div><i class="go"></i></li>
    <li><i class="ic"></i><div class="tx"><b>Agri Sense</b><span>Soil sensors for small farms</span></div><i class="go"></i></li>
    <li><i class="ic"></i><div class="tx"><b>Code Nest</b><span>Coding tools for new learners</span></div><i class="go"></i></li>
  </ul>
  <div class="more"></div>
</section>
<section class="abs card" style="left:369px">
  <h3>SPONSORED COMPANIES</h3>
  <ul>
    <li><i class="ic"></i><div class="tx"><b>Northwave</b><span>Industrial research partner</span></div><i class="go"></i></li>
    <li><i class="ic"></i><div class="tx"><b>Corelign</b><span>Medical device investor</span></div><i class="go"></i></li>
    <li><i class="ic"></i><div class="tx"><b>Fieldstone</b><span>Venture growth fund</span></div><i class="go"></i></li>
    <li><i class="ic"></i><div class="tx"><b>Pelora</b><span>Consumer goods innovation</span></div><i class="go"></i></li>
    <li><i class="ic"></i><div class="tx"><b>Vantis</b><span>Software and data group</span></div><i class="go"></i></li>
  </ul>
  <div class="more"></div>
</section>

<section class="abs intro">
  <h2>CHANGE THE WAY YOU <em>INNOVATE</em></h2>
  <div class="rule"></div>
  <p>Brightmarket connects student founders with senior research and acquisition leaders. Browse new ventures, follow promising teams and start conversations early. Schools list their best startups, sponsors discover fresh ideas, and every match begins with a simple profile that tells the story of the company, its market and its people.</p>
</section>
<div class="abs bulb-art" role="img" aria-label="Faint line illustration of a light bulb"></div>

<svg class="abs band" viewBox="0 0 726 140" preserveAspectRatio="none"><polygon points="0,0 726,30 726,110 0,140" fill="var(--navy)"/><polygon points="0,12 726,36 726,104 0,128" fill="var(--blue)"/></svg>
<div class="abs tiles">
  <div class="tile"><i style="background:var(--navy)"></i></div>
  <div class="tile"><i style="background:#8a1c2b;border-radius:50%"></i></div>
  <div class="tile"><i style="background:#c8102e"></i></div>
  <div class="tile"><i style="background:#7a1a1a"></i></div>
  <div class="tile"><i style="background:#d22;border-radius:50%"></i></div>
  <div class="tile"><i style="background:#c8102e"></i></div>
</div>

<section class="abs app">
  <h2>THE <em>BRIGHTMARKET</em> APPLICATION</h2>
  <div class="rule"></div>
  <p>Show the companies with the most market promise and invite partners to the Tradeloop Platform. A short walkthrough explains how schools submit ventures and how sponsors review them.</p>
  <p>It is very important that you provide as much detail as you can during the application process. We want to learn about unique and protectable innovation, market size, competitors and roadmap.</p>
  <p>Journals of interest and estimated milestones for completion of certain milestones. Click here for examples of business plan templates.</p>
  <div class="btns"><div class="btn or">MORE APPLICATION</div><div class="btn gr">SIGN UP</div></div>
</section>
<div class="abs video">
  <div class="ttl">YOUR VIDEO - FULL HEAD</div>
  <div class="abs stage"><svg width="60" height="60" viewBox="0 0 60 60"><circle cx="30" cy="30" r="26" fill="none" stroke="var(--soft)" stroke-width="3"/><polygon points="24,18 42,30 24,42" fill="var(--navy)"/></svg></div>
  <div class="abs ctrl"><svg width="8" height="8"><polygon points="0,0 8,4 0,8" fill="#fff"/></svg><i></i></div>
</div>

<div class="abs follow"><span>CHANGE THE WAY YOU INNOVATE. FOLLOW US.</span><div class="soc"><span></span><span></span><span></span><span></span></div></div>
<footer class="abs footer">
  <div class="col fbrand"><div class="brand"><i></i>Brightmarket</div><p>Linking campus ventures with the teams that help them grow, one clear profile at a time.</p></div>
  <div class="col"><h4>QUICK LINKS</h4>Home<br>Join for Schools<br>My Schools<br>Student Companies<br>About</div>
  <div class="col"><h4>OUR SERVICES</h4>Startup Listings<br>Sponsor Search<br>Deal Rooms<br>Event Calendar<br>Reports</div>
  <div class="col"><h4>CONTACT US</h4>120 Harbor Street<br>Suite 400, Lakeview<br>(555) 014-2290<br>hello@brightmarket.example</div>
</footer>
<div class="abs copy">© Brightmarket. All Rights Reserved.</div>
</body>
</html>
```